Promotional poster for a vintage motorcycle show.

Vertically oriented, based on 11 x 17 inch proportions

Though not to the exclusion of other design concepts, stylistically perhaps something evoking a vintage (early-mid 20th century) 2-3 color silk screen style event poster.

In addition to some sort of eyecatching, vintage / antique motorbike oriented graphic (preferably not Corwin Baxley based), the poster should include the following text and info:

3rd Annual Milo Quenby Vintage Motorcycle Show
Bordentown City, N.J.
October 1st (rain date Oct. 2nd)
11am-4pm

Presented in conjunction with the 27th Annual Thistlewood Fair

For further info, or to register your pre-1992 bike contact:
Marty@wheelvaultex.com or 555-204-8913

Sponsored by:
UptownHallowmereGuildway.com
Wheelvaultex.com

Must have
• See above project description
Nice to have
• See above project describtion

```html
<!DOCTYPE html>
<html lang="en">
<head>
<meta charset="UTF-8">
<title>3rd Annual Milo Quenby Vintage Motorcycle Show</title>
<link rel="stylesheet" href="https://fonts.googleapis.com/css2?family=Lobster&family=Arimo:wght@400;700&display=swap">
<style>
  :root {
    --gold: #e3b02a;
    --gold-light: #f6d463;
    --gold-deep: #d39c1d;
    --ink: #3a3522;
    --ribbon: #6b3f26;
    --ribbon-dark: #4a2a18;
    --tan: #c99a5c;
    --chevron: #f7e08a;
    --white: #fff8e6;
  }
  * { margin: 0; padding: 0; box-sizing: border-box; }
  html, body { width: 778px; height: 1200px; overflow: hidden; }
  body { background: var(--gold); font-family: "Arimo", Arial, sans-serif; color: var(--ink); }
  .poster {
    position: relative; width: 778px; height: 1200px; overflow: hidden;
    background: radial-gradient(ellipse at 50% 42%, var(--gold-light) 0%, var(--gold) 55%, var(--gold-deep) 100%);
  }
  .banner { position: absolute; left: 0; top: 20px; width: 778px; height: 90px; }
  .banner-edition, .banner-host {
    position: absolute; left: 0; width: 778px; text-align: center; text-transform: none;
  }
  .banner-edition { top: 28px; font-size: 22px; color: var(--white); letter-spacing: 0.5px; }
  .banner-host { top: 60px; font-size: 24px; color: var(--white); letter-spacing: 1px; text-transform: uppercase; }
  .title {
    position: absolute; left: 0; width: 778px; text-align: center;
    font-family: "Lobster", cursive; color: var(--ink); line-height: 1;
  }
  .title-vintage { top: 118px; font-size: 128px; }
  .title-motorcycle { top: 222px; font-size: 128px; }
  .title-show { top: 318px; font-size: 118px; }
  .chevrons { position: absolute; top: 356px; width: 110px; height: 62px; }
  .chevrons.left { left: 170px; }
  .chevrons.right { left: 500px; }
  .date {
    position: absolute; top: 430px; left: 0; width: 778px; text-align: center;
    font-weight: 700; font-size: 56px; letter-spacing: 0.5px;
  }
  .date sup { font-size: 28px; vertical-align: 26px; }
  .rain-date, .hours {
    position: absolute; left: 0; width: 778px; text-align: center; font-weight: 700; font-size: 22px;
  }
  .rain-date { top: 492px; }
  .hours { top: 518px; }
  .location {
    position: absolute; top: 570px; left: 0; width: 778px; text-align: center;
    font-weight: 700; font-size: 28px; letter-spacing: 0.5px;
  }
  .bike-art {
    position: absolute; top: 620px; left: 90px; width: 610px; height: 300px; border-radius: 40px;
    background: radial-gradient(ellipse at 50% 55%, rgba(58,53,34,0.55) 0%, rgba(58,53,34,0.25) 60%, rgba(58,53,34,0) 100%);
  }
  .credits {
    position: absolute; top: 928px; left: 0; width: 778px; text-align: center;
    font-size: 19px; line-height: 22px;
  }
  .contact {
    position: absolute; top: 1090px; left: 0; width: 778px; text-align: center;
    font-size: 19px; line-height: 24px;
  }
  .chevrons.small { top: 1094px; width: 64px; height: 44px; }
  .chevrons.small.left { left: 66px; }
  .chevrons.small.right { left: 648px; }
</style>
</head>
<body>
<main class="poster">
  <svg class="banner" viewBox="0 0 778 90" aria-hidden="true">
    <polygon points="120,10 200,10 200,48 120,48 140,29" fill="var(--ribbon-dark)"/>
    <polygon points="658,10 578,10 578,48 658,48 638,29" fill="var(--ribbon-dark)"/>
    <rect x="160" y="0" width="458" height="40" fill="var(--ribbon)"/>
    <rect x="262" y="40" width="254" height="46" fill="var(--tan)"/>
  </svg>
  <p class="banner-edition">3rd Annual</p>
  <p class="banner-host">Milo Quenby</p>

  <h1>
    <span class="title title-vintage">Vintage</span>
    <span class="title title-motorcycle">Motorcycle</span>
    <span class="title title-show">Show</span>
  </h1>

  <svg class="chevrons left" viewBox="0 0 110 62" aria-hidden="true">
    <polygon points="0,0 22,0 48,31 22,62 0,62 26,31" fill="var(--chevron)"/>
    <polygon points="46,0 68,0 94,31 68,62 46,62 72,31" fill="var(--chevron)"/>
  </svg>
  <svg class="chevrons right" viewBox="0 0 110 62" aria-hidden="true">
    <polygon points="110,0 88,0 62,31 88,62 110,62 84,31" fill="var(--chevron)"/>
    <polygon points="64,0 42,0 16,31 42,62 64,62 38,31" fill="var(--chevron)"/>
  </svg>

  <p class="date">OCTOBER 1<sup>st</sup></p>
  <p class="rain-date">(rain date Oct. 2nd)</p>
  <p class="hours">11am-4pm</p>
  <p class="location">BORDENTOWN CITY, N.J.</p>

  <div class="bike-art" role="img" aria-label="Dark silhouette of a vintage motorcycle in side view"></div>

  <p class="credits">
    Presented in conjunction with the<br>
    27th Annual Thistlewood Fair<br>
    Sponsored by:<br>
    UptownHallowmereGuildway.com<br>
    Wheelvaultex.com
  </p>

  <svg class="chevrons small left" viewBox="0 0 64 44" aria-hidden="true">
    <polygon points="0,0 14,0 30,22 14,44 0,44 16,22" fill="var(--chevron)"/>
    <polygon points="28,0 42,0 58,22 42,44 28,44 44,22" fill="var(--chevron)"/>
  </svg>
  <p class="contact">
    For further info, or to register your pre-1992 bike contact:<br>
    Marty@wheelvaultex.com or 555-204-8913
  </p>
  <svg class="chevrons small right" viewBox="0 0 64 44" aria-hidden="true">
    <polygon points="64,0 50,0 34,22 50,44 64,44 48,22" fill="var(--chevron)"/>
    <polygon points="36,0 22,0 6,22 22,44 36,44 20,22" fill="var(--chevron)"/>
  </svg>
</main>
</body>
</html>
```